Business card design needed

the business is HR Consulting, but its for SME businesses who cant afford a permanent HR person. We sell an HR info system to help them meet minimum employment legislation but with this hope they then require us on a monthly subscription to phone or email us for HR advice. We are HR qualified mums working from home

So we will be partners to HR and Payroll systems known as kindle HR and Pluto

Target Market(s)

Small to medium businesses so not black and overly corporate, but having said that many are accounting businesses

Industry/Entity Type

Business

Contact Information for Business Card

Name of the company: Quillmere HR

Me:Marta Kovalenko
Title:Managing Director

m: 0437 215 683
e: marta@quillmerehr.com.au
w: www.quillmerehr.com.au

What we do: HR Consulting, HR Systems and support, Payroll Advice

Requirements
Nice to have
• there is a company already out there known as Quartz professionals. I like the leaves at the end as I wanted something different like this to the usual business logos but still professional. I wanted a symbol to show calm, positive, ease flow going up ,etc. but realise they have the leaves and possibly cant copy, or can we?..( kite??, something calm and positive)dont know!!. Green and blue needed to be in it as nature and calm as well. I love the colours of www.stafflanefund.com ( attached the colours), as well as the calm wave line underneath. have a look as while they use green and blue I loved the purple colour thrown in there.Green and blue on their own are so overused. I want vibrant. I want double sided and when on a table I want it to stand out so maybe the purple colour (as per the colours on the fund website) solid on one side with just the 3 services we provide and personal and company name on front but need some creativity from you guys.

```html
<!DOCTYPE html>
<html lang="en">
<head>
<meta charset="utf-8">
<title>Quillmere HR – Business Card</title>
<link rel="stylesheet" href="https://fonts.googleapis.com/css2?family=Titillium+Web:ital,wght@0,400;0,600;0,700;1,400&display=swap">
<style>
  :root {
    --bg: #e9e6e1;
    --teal: #1f9ba3;
    --teal-deep: #15808a;
    --teal-text: #17828c;
    --paper: #f3f4f5;
    --plum: #8c2b72;
    --lime: #c6d67c;
    --white: #ffffff;
    --white-soft: rgba(255,255,255,0.85);
    --shadow: 0 10px 28px rgba(40,30,20,0.22);
  }
  * { box-sizing: border-box; margin: 0; padding: 0; }
  html, body { width: 1200px; height: 880px; overflow: hidden; }
  body {
    background: var(--bg);
    font-family: "Titillium Web", sans-serif;
    position: relative;
  }
  .card {
    position: absolute;
    top: 275px;
    width: 540px;
    height: 330px;
    border-radius: 4px;
    box-shadow: var(--shadow);
    overflow: hidden;
  }

  /* Front face */
  .card--front {
    left: 40px;
    background: var(--paper);
  }
  .front__web {
    position: absolute;
    left: 48px;
    top: 132px;
    font-size: 21px;
    letter-spacing: 2px;
    color: var(--teal-text);
    white-space: nowrap;
  }
  .front__web strong { font-weight: 700; }
  .front__brand {
    position: absolute;
    right: 40px;
    bottom: 48px;
    display: flex;
    align-items: center;
    gap: 12px;
  }
  .brand__dot {
    width: 24px;
    height: 24px;
    border-radius: 50%;
    background: var(--plum);
    flex: none;
  }
  .brand__name {
    font-weight: 700;
    line-height: 1;
    white-space: nowrap;
  }
  .front__brand .brand__name {
    font-size: 36px;
    color: var(--teal-text);
  }

  /* Back face */
  .card--back {
    left: 620px;
    background: linear-gradient(135deg, var(--teal) 0%, var(--teal-deep) 100%);
    color: var(--white);
  }
  .back__brand {
    position: absolute;
    left: 32px;
    top: 110px;
    display: flex;
    align-items: center;
    gap: 10px;
  }
  .back__brand .brand__dot { background: var(--lime); width: 18px; height: 18px; }
  .back__brand .brand__name {
    font-size: 28px;
    color: var(--white);
  }
  .back__divider {
    position: absolute;
    left: 264px;
    top: 40px;
    width: 1px;
    height: 190px;
    background: var(--white-soft);
  }
  .contact {
    position: absolute;
    left: 288px;
    top: 46px;
  }
  .contact__name {
    font-size: 22px;
    font-weight: 700;
    line-height: 1.1;
    white-space: nowrap;
  }
  .contact__title {
    font-size: 16px;
    font-style: italic;
    color: var(--white-soft);
    margin-bottom: 22px;
  }
  .contact__list { list-style: none; }
  .contact__item {
    display: flex;
    align-items: center;
    gap: 10px;
    font-size: 16px;
    line-height: 1.6;
    letter-spacing: 0.3px;
    white-space: nowrap;
  }
  .contact__icon { width: 14px; height: 14px; flex: none; }
  .back__services {
    position: absolute;
    left: 32px;
    right: 24px;
    bottom: 28px;
    font-size: 13px;
    letter-spacing: 1.6px;
    color: var(--white-soft);
    white-space: nowrap;
  }
</style>
</head>
<body>

  <section class="card card--front" aria-label="Business card front">
    <p class="front__web">www.<strong>quillmerehr</strong>.com.au</p>
    <div class="front__brand">
      <span class="brand__dot"></span>
      <span class="brand__name">Quillmere HR</span>
    </div>
  </section>

  <section class="card card--back" aria-label="Business card back">
    <div class="back__brand">
      <span class="brand__dot"></span>
      <span class="brand__name">Quillmere HR</span>
    </div>
    <div class="back__divider"></div>
    <div class="contact">
      <p class="contact__name">Marta Kovalenko</p>
      <p class="contact__title">Managing Director</p>
      <ul class="contact__list">
        <li class="contact__item">
          <svg class="contact__icon" viewBox="0 0 14 14" fill="none" stroke="#fff" stroke-width="1.3"><rect x="3.5" y="1" width="7" height="12" rx="1.2"/><line x1="6" y1="11" x2="8" y2="11"/></svg>
          0437 215 683
        </li>
        <li class="contact__item">
          <svg class="contact__icon" viewBox="0 0 14 14" fill="none" stroke="#fff" stroke-width="1.3"><rect x="1" y="3" width="12" height="8.5" rx="0.8"/><polyline points="1,3.5 7,8 13,3.5"/></svg>
          marta@quillmerehr.com.au
        </li>
        <li class="contact__item">
          <svg class="contact__icon" viewBox="0 0 14 14" fill="none" stroke="#fff" stroke-width="1.2"><circle cx="7" cy="7" r="5.8"/><ellipse cx="7" cy="7" rx="2.6" ry="5.8"/><line x1="1.2" y1="7" x2="12.8" y2="7"/></svg>
          www.quillmerehr.com.au
        </li>
      </ul>
    </div>
    <p class="back__services">HR Consulting . HR Systems and training . Payroll support</p>
  </section>

</body>
</html>
```